International professional tennis coach needs a book cover design

This is my 2nd published book, the first one was a #1 on the best seller. I'm looking for a world class book cover design for this new book. The name of my first book was 5 Baseline Habits to Unlock Your Rally Rhythm, located on Brimlow.com

The title of the new book:

Title: The Craft of Steady Rallies
Subtitle: Building a Tactical Margin by Way of Opponent Insight

I'm uploading our new CRAFT OF STEADY logo that I'd like for you to use as the centerpiece of the book design along with a 21st century design feel that incorporates what the book topic is below::

--> This book is about building competitive intelligence by using tennis data analytics to develop and expand a player's strategic advantage for match play. <--

The colors we would like to use are Blue, Yellow, and Green. These shades of these colors should be bold! (You will see the bold color examples of blues, yellows, and greens that I'm talking about in the logos that are attached here, especially the colors for my Tennis GridRally App logo.

I will upload the Tennis GridRally logo which should go somewhere on the back cover design (small size maybe in the bottom corner).

This book is revolutionary to the standard way of teaching tennis, it is based on a decade of recording and gathering tennis data analytics and then we created on-court practice games to develop better decision making in players for the competitive edge.

My websites are www.elevatedrillzone.com and www.craftofsteadyrallies.com

```html
<!DOCTYPE html>
<html lang="en">
<head>
<meta charset="utf-8">
<title>The Craft of Steady Rallies — Book Cover</title>
<link rel="stylesheet" href="https://fonts.googleapis.com/css2?family=Oswald:wght@300;600;700&display=swap">
<style>
  :root {
    --backdrop: #e4e4e4;
    --paper: #f2f2f2;
    --ink: #2a2a2a;
    --brand-blue: #2f6fd0;
    --brand-yellow: #f0c030;
    --band-text: #ffffff;
  }
  * { margin: 0; padding: 0; box-sizing: border-box; }
  html, body {
    width: 1200px;
    height: 1000px;
    overflow: hidden;
    background: var(--backdrop);
  }
  .book-cover {
    position: absolute;
    left: 372px;
    top: 172px;
    width: 458px;
    height: 643px;
    background: var(--paper);
    font-family: "Oswald", sans-serif;
    color: var(--ink);
  }
  .title {
    position: absolute;
    top: 100px;
    left: 0;
    width: 100%;
    text-align: center;
    font-weight: 700;
    color: var(--ink);
    line-height: 1;
  }
  .title-lead { display: block; font-size: 26px; margin-bottom: 2px; }
  .title-main { display: block; font-size: 92px; letter-spacing: -1px; line-height: 0.95; }
  .title-tail { display: block; font-size: 30px; margin-top: 2px; }
  .emblem {
    position: absolute;
    left: 164px;
    top: 262px;
    width: 130px;
    height: 130px;
  }
  .subtitle {
    position: absolute;
    top: 454px;
    left: 0;
    width: 100%;
    text-align: center;
    font-weight: 300;
    font-size: 23px;
    line-height: 32px;
  }
  .author-band {
    position: absolute;
    left: 0;
    bottom: 0;
    width: 100%;
    height: 47px;
    background: var(--brand-blue);
    display: flex;
    align-items: center;
    justify-content: center;
  }
  .author-name {
    color: var(--band-text);
    font-weight: 600;
    font-size: 23px;
    letter-spacing: 2px;
  }
</style>
</head>
<body>
  <main class="book-cover">
    <h1 class="title">
      <span class="title-lead">The Craft of</span>
      <span class="title-main">Steady</span>
      <span class="title-tail">Rallies</span>
    </h1>
    <svg class="emblem" viewBox="0 0 130 130" aria-hidden="true">
      <circle cx="65" cy="65" r="65" fill="var(--brand-blue)"/>
    </svg>
    <p class="subtitle">Building a Tactical Margin<br>by Way of Opponent Insight</p>
    <footer class="author-band">
      <span class="author-name">CORWIN HALDANE</span>
    </footer>
  </main>
</body>
</html>
```